Premium Gold Vodka Label Design

English ------------------- We need a label for a Vodka Bottle. Its a sparkling premium vodka with gold inside. The design should look premium. We tried it on our selves but it looks horrible. Therefore we need your help. The current name is corvelle K, but we are open for any better suggestion. We attached the selfmade design. The label will be printed on the bottle. We have other design jobs for you (logo, other sorts)! English ------------------------ We need a label for a vodka bottle. This is a premium vodka which is offset with gold. The design should look like this. We have tried so far and failed. That is why we need your support. The name is so far corvelle K. If you have better suggestions we would be pleased about other suggestions / ideas. In the appendix the failed design is stored. The label is to be applied by screen printing. In the case of good work follow-up projects are guaranteed (logo, other varieties, etc)!
Updates

Reason: We need more time for the decision.

Target Market(s)

USA

Colors

Designer to choose colors to be used in the design.

Requirements
Must have
• English ------------------------ The needed text is on our selfmade label that is attached. English ------------------------ The required texts are stored in the attached design.
Nice to have
• English ------------------------ Transparent places are allowed because we want to print the label on the bottom. English ------------------------ As the label is applied by screen printing, transparent areas are also possible.

```html
<!DOCTYPE html>
<html lang="en">
<head>
<meta charset="utf-8">
<title>Corvelle K Vodka Label</title>
<link href="https://fonts.googleapis.com/css2?family=Teko:wght@300;400;500;600&display=swap" rel="stylesheet">
<style>
  :root {
    --label-black: #000000;
    --gold: #e6c22a;
    --gold-light: #f5e27a;
    --gold-deep: #b8901a;
  }
  html, body {
    margin: 0;
    padding: 0;
    width: 696px;
    height: 1200px;
    overflow: hidden;
    background: var(--label-black);
  }
  .label {
    position: relative;
    width: 696px;
    height: 1200px;
    background: var(--label-black);
    font-family: "Teko", "Arial Narrow", sans-serif;
    color: var(--gold);
    text-transform: uppercase;
  }
  .rule {
    position: absolute;
    left: 0;
    width: 696px;
    height: 20px;
  }
  .brand-name {
    position: absolute;
    top: 30px;
    left: 0;
    width: 696px;
    margin: 0;
    text-align: center;
    font-weight: 600;
    font-size: 138px;
    line-height: 150px;
    letter-spacing: 2px;
    color: var(--gold);
  }
  .product-type {
    position: absolute;
    top: 218px;
    left: 0;
    width: 696px;
    text-align: center;
    font-weight: 300;
    font-size: 100px;
    line-height: 100px;
    letter-spacing: 4px;
  }
  .karat {
    position: absolute;
    top: 522px;
    left: 0;
    width: 696px;
    text-align: center;
    font-weight: 600;
    font-size: 56px;
    line-height: 56px;
  }
  .descriptor {
    position: absolute;
    left: 0;
    width: 696px;
    text-align: center;
    font-weight: 300;
    font-size: 54px;
    line-height: 54px;
    letter-spacing: 0.5px;
    word-spacing: 4px;
  }
  .descriptor strong { font-weight: 600; }
  .sparkling { top: 636px; }
  .distilled { top: 854px; }
  .origin { top: 916px; }
  .spec-row {
    position: absolute;
    top: 1130px;
    left: 0;
    width: 696px;
    display: flex;
    justify-content: center;
    align-items: center;
    font-weight: 500;
    font-size: 38px;
    line-height: 40px;
  }
  .spec-divider {
    display: inline-block;
    width: 3px;
    height: 44px;
    background: var(--gold);
    margin: 0 34px;
  }
</style>
</head>
<body>
  <div class="label">
    <svg class="rule" style="top:17px" viewBox="0 0 696 20" aria-hidden="true">
      <line x1="118" y1="10" x2="582" y2="10" stroke="var(--gold)" stroke-width="2.5"/>
      <rect x="342" y="2" width="12" height="12" transform="rotate(45 348 8)" fill="var(--gold-light)"/>
    </svg>

    <h1 class="brand-name">Corvelle K</h1>

    <svg class="rule" style="top:174px" viewBox="0 0 696 20" aria-hidden="true">
      <line x1="184" y1="10" x2="516" y2="10" stroke="var(--gold)" stroke-width="2.5"/>
      <rect x="342" y="6" width="12" height="12" transform="rotate(45 348 12)" fill="var(--gold-light)"/>
    </svg>

    <div class="product-type">Vodka</div>

    <div class="karat">24 KT</div>

    <svg class="rule" style="top:597px" viewBox="0 0 696 20" aria-hidden="true">
      <line x1="137" y1="10" x2="310" y2="10" stroke="var(--gold)" stroke-width="4"/>
      <line x1="386" y1="10" x2="560" y2="10" stroke="var(--gold)" stroke-width="4"/>
    </svg>
    <svg class="rule" style="top:597px" viewBox="0 0 696 20" role="img" aria-label="Small gold ribbon flourish">
      <rect x="312" y="3" width="72" height="14" rx="3" fill="var(--gold-deep)"/>
    </svg>

    <div class="descriptor sparkling">Premium Gold&nbsp; Sparkling</div>

    <div class="descriptor distilled">Distilled <strong>8</strong> Filtered</div>
    <div class="descriptor origin">Made in Germany</div>

    <svg class="rule" style="top:975px" viewBox="0 0 696 20" aria-hidden="true">
      <line x1="137" y1="10" x2="310" y2="10" stroke="var(--gold)" stroke-width="4"/>
      <line x1="386" y1="10" x2="560" y2="10" stroke="var(--gold)" stroke-width="4"/>
    </svg>
    <svg class="rule" style="top:975px" viewBox="0 0 696 20" role="img" aria-label="Small gold ribbon flourish">
      <rect x="312" y="3" width="72" height="14" rx="3" fill="var(--gold-deep)"/>
    </svg>

    <div class="spec-row">
      <span class="spec">40% Alc Vol</span>
      <span class="spec-divider"></span>
      <span class="spec">200 ml</span>
      <span class="spec-divider"></span>
      <span class="spec">80 Proof</span>
    </div>
  </div>
</body>
</html>
```